Flyer Design Project for Wellgrove Mind Clinic

We are a psychology clinic that specialises in eating, parenting and chronic illness & pain. See our website for a summary.

We need a flyer that will go to doctors and schools in the local area.

Things to include on the front page:

Immediate appointments available
After hours appointments available
Male and female psychologists

Phone 9362 5184
Web wellgrovemindclinic.com.au

On the back page:

Phone 9362 5184
Suite 2/1187 Ferntree Rd, Ashbury Vale 3142.
wellgrovemindclinic.com.au

Parenting: Parenthood is an amazing journey, but for lots of people it raises all sorts of issues from fear of birth, breastfeeding difficulties and settling problems, to toddler discipline and food fussiness all the way through to getting help for your depressed or anxious adolescent. Our Parenting Psychologists can help you be the best parent you can be which will in turn lead to happier families, homes, children and parents.

Chronic illness/pain: Diabetes, heart disease, arthritis, asthma, migraines, dizziness, chronic fatigue syndrome, infertility, and PCOS are just some of the conditions that can be managed with psychological interventions. Everything we do is about helping you to manage your condition and get back to focusing on what you really want your life to be about.

Eating: Whether you suffer from anorexia, bulimia or binge eating, our strategies help you develop a healthy relationship with food and your body. The practical tips and strategies that we can provide are very useful for people undergoing lapband surgery or liposuction.

I am interested in whether the photographs that I have already purchased can be used...so please have a look through the website and see which you think will suit your design. Photographs are not absolutely necessary though, so if it doesn't fit with your idea that is okay too.
Updates

HI Everyone,

Thanks for submitting so far! I haven't found anything yet that has hit the mark. And I am thinking that is my fault and maybe that way i have described what I want. I apologise and hope that this update might help.

This brochure is likely to sit with lots of other brochures in a doctors waiting room so it needs to be different - so that it will be noticed.

The majority of our market are women - so something feminine is important. Maybe it needs to be a little more playful that I had initially thought. Like maybe not your standard blocky text and bolds and primary colours. But something more creative, more personal.

I want to not focus just on the family theme. Parenting is one area that we cover, but also we help people with eating disorders and chronic illness/chronic pain. So the photographs that I use need to be more general. It is importnat to focus on happy and healthy looking people. As we went to appeal to what my potential clients want to look like and feel like.

I do hope this helps to guide you. I promise that once I see a flyer that I could choose, I will turn the funding to guaranteed. I did this last time...I am just a bit nervous as I haven't received anything yet that I am excited about.

Kindest regards,

Marietta.

Hi Everyone,

Thank you for your designs coming in! As promised, as soon as I received a design that I could see myself choosing I would change the status from refundable to committed. I have now done this!

I have received a design that I would say is good. It is not perfect however...so please keep the ideas coming.

To give more direction, the one that came in has a nice theme that runs through the brochure. Not too many different types of font and colours detracting from the flow of the flyer. However, the thing that I am concerned about is whether it will stand out enough on a rack of other flyers in a doctors waiting room.

I hope this helps with your creative ideas.

Thanks again to everyone!

Marietta.

Thanks SO much to everyone who is putting in designs. You are making my decision difficult!

I am wondering if you can update your designs with a few things:

can I ask you to make some text changes:

1. Can we have a heading on the front page: Psychologists  and then can you put Ashbury Vale in smaller writing just below it?

2. Id like to say on the front: Specialising in parenting, disordered eating and chronic pain & illness

3. Delete Male & Female Psychologists

4. In general we dont' need to have the logo standing out. We don't have a well known brand yet, so I am not wanting to take up valuable space with this - so perhaps it shoudl be small and maybe just on the back? Keeping the name of our clinic on the front with the website shoudl be sufficient.

Thanks heaps everyone...I will make decision very soon!

Target Market(s)

20-40 year olds. Working. Educated. Female. They might have a family/children.
Australian. Engish speaking.

Industry/Entity Type

Clinic

Requirements
Must have
• I would like to include our logo. Please do not use the colour green that it is in. I hate that colour! but I LOVE the logo.

I would like to follow through with some of the themes of the website and other stationary.

I will attach some of the other stationary I have had designed.

I really like the colours in the letterhead - especially that blue of the logo.

I think it needs to have a dash of colour with it at least...something that will stand out and be noticed on a brochure rack...but also have a look of class/sophistication/modern.
Nice to have
• Perhaps photograph of happy and healthy people.
Should not have
• I don't like bold text or too many different types of fonts.

It shouldn't look too cluttered so I might need to reduce the text I have included - I will need to see it first.

```html
<!DOCTYPE html>
<html lang="en">
<head>
<meta charset="utf-8">
<title>Wellgrove Mind Clinic – Flyer</title>
<link rel="stylesheet" href="https://fonts.googleapis.com/css2?family=Open+Sans:wght@400;600&display=swap">
<style>
  :root{
    --teal-deep:#1b6e6b;
    --teal-dark:#23807c;
    --teal-mid:#4fa39e;
    --teal-light:#86c7c2;
    --teal-pale:#cfe8e5;
    --slate:#6f8088;
    --slate-light:#9aa7ad;
    --sky-top:#7fb9e0;
    --sky-low:#d9ecf6;
    --ink:#55626a;
    --paper:#ffffff;
    --backdrop:#eceff0;
  }
  *{box-sizing:border-box;margin:0;padding:0}
  html,body{width:1200px;height:811px;overflow:hidden;background:var(--backdrop)}
  body{font-family:"Open Sans",Arial,sans-serif;color:var(--ink);position:relative}

  .flyer{position:absolute;top:15px;width:330px;height:780px;background:var(--paper);overflow:hidden;box-shadow:0 2px 10px rgba(0,0,0,.15)}
  .flyer--front{left:245px}
  .flyer--back{left:625px}
  .flyer__shapes{position:absolute;inset:0}

  .brand{position:absolute;display:flex;align-items:center;gap:8px;color:var(--teal-mid);font-weight:400;text-transform:uppercase;letter-spacing:.14em;line-height:1.25}
  .brand__dot{width:22px;height:22px;border-radius:50%;background:var(--teal-light);flex:none}
  .brand--small{top:28px;left:18px;font-size:9px}
  .brand--small .brand__dot{width:16px;height:16px}
  .brand--large{font-size:12px}
  .brand--large .brand__dot{width:34px;height:34px}

  .photo{position:absolute;left:0;top:14px;width:330px;height:331px;
    background:linear-gradient(180deg,var(--sky-top),var(--sky-low) 70%,#eef3f2);
    clip-path:polygon(0 0,100% 0,100% 86%,0 100%)}

  .headline{position:absolute;left:12px;top:352px;color:#fff;font-weight:400;font-size:19px;line-height:1.15}
  .availability{position:absolute;left:12px;top:440px;color:#fff}
  .availability__title{font-size:16px;font-weight:400;margin-bottom:8px}
  .availability__list{list-style:none;font-size:7.6px;font-weight:600;letter-spacing:.04em;text-transform:uppercase}
  .availability__list li{display:flex;align-items:center;gap:6px;margin-bottom:7px}

  .contact{position:absolute;display:flex;align-items:center;gap:6px}
  .contact svg{flex:none}
  .contact--web{font-size:11px}
  .contact--phone{font-size:17px}
  .front-web{right:14px;top:645px;color:var(--teal-deep);flex-direction:row}
  .front-phone{right:14px;top:668px;color:var(--teal-deep)}

  .services{position:absolute;left:20px;right:20px;top:38px}
  .service{margin-bottom:14px}
  .service__title{color:var(--teal-dark);font-weight:400;font-size:13px;margin-bottom:4px}
  .service__text{font-size:8.6px;line-height:1.6;color:var(--ink)}

  .back-web{left:16px;top:425px;color:#fff}
  .back-address{left:16px;top:482px;color:#fff;font-size:11px;line-height:1.4;align-items:flex-start}
  .back-phone{left:16px;top:530px;color:#fff}
</style>
</head>
<body>

<!-- Front page -->
<section class="flyer flyer--front" aria-label="Flyer front page">
  <svg class="flyer__shapes" width="330" height="780" viewBox="0 0 330 780" aria-hidden="true">
    <g class="colour-strip">
      <rect x="0" y="0" width="55" height="14" fill="#6fb4ae"/>
      <rect x="55" y="0" width="55" height="14" fill="#4d8f8b"/>
      <rect x="110" y="0" width="55" height="14" fill="#9fd2cd"/>
      <rect x="165" y="0" width="55" height="14" fill="#3f7f7c"/>
      <rect x="220" y="0" width="55" height="14" fill="#7a8a8f"/>
      <rect x="275" y="0" width="55" height="14" fill="#4fa39e"/>
    </g>
    <polygon points="0,345 330,300 330,470 0,620" fill="var(--teal-light)"/>
    <polygon points="0,345 210,345 240,418 0,418" fill="var(--teal-dark)"/>
    <polygon points="240,418 330,418 330,476" fill="var(--teal-deep)"/>
    <polygon points="0,418 240,418 120,560 0,560" fill="var(--teal-mid)" opacity=".55"/>
    <polygon points="0,620 0,752 110,752" fill="var(--teal-pale)"/>
    <polygon points="0,680 0,752 50,752" fill="var(--teal-light)"/>
    <g class="colour-strip">
      <rect x="0" y="752" width="110" height="28" fill="var(--teal-light)"/>
      <rect x="110" y="752" width="110" height="28" fill="var(--teal-mid)"/>
      <rect x="220" y="752" width="110" height="28" fill="var(--slate)"/>
    </g>
  </svg>

  <div class="photo" role="img" aria-label="Photo of a smiling family of four in white clothes against a blue sky"></div>

  <div class="brand brand--small"><span class="brand__dot"></span><span>Wellgrove<br>Mind Clinic</span></div>

  <h1 class="headline">Being the Best<br>Parent you can be</h1>

  <div class="availability">
    <h2 class="availability__title">Availability</h2>
    <ul class="availability__list">
      <li><svg width="6" height="8" viewBox="0 0 6 8"><path d="M1 1l3 3-3 3" stroke="#fff" stroke-width="1.4" fill="none"/></svg>Male and female psychologists</li>
      <li><svg width="6" height="8" viewBox="0 0 6 8"><path d="M1 1l3 3-3 3" stroke="#fff" stroke-width="1.4" fill="none"/></svg>Immediate appointments</li>
      <li><svg width="6" height="8" viewBox="0 0 6 8"><path d="M1 1l3 3-3 3" stroke="#fff" stroke-width="1.4" fill="none"/></svg>After hours appointments</li>
    </ul>
  </div>

  <div class="brand brand--large" style="left:140px;top:585px"><span class="brand__dot"></span><span>Wellgrove<br>Mind<br>Clinic</span></div>

  <p class="contact contact--web front-web">wellgrovemindclinic.com.au
    <svg width="11" height="11" viewBox="0 0 12 12"><circle cx="6" cy="6" r="5.3" fill="var(--teal-deep)"/><path d="M1 6h10M6 1c-2 2.5-2 7.5 0 10M6 1c2 2.5 2 7.5 0 10" stroke="#fff" stroke-width=".8" fill="none"/></svg>
  </p>
  <p class="contact contact--phone front-phone">9362 5184
    <svg width="8" height="13" viewBox="0 0 8 13"><path d="M2 1.5c3 1 4 6 0 10" stroke="var(--teal-deep)" stroke-width="2" fill="none" stroke-linecap="round"/></svg>
  </p>
</section>

<!-- Back page -->
<section class="flyer flyer--back" aria-label="Flyer back page">
  <svg class="flyer__shapes" width="330" height="780" viewBox="0 0 330 780" aria-hidden="true">
    <g class="colour-strip">
      <rect x="0" y="0" width="55" height="14" fill="#6fb4ae"/>
      <rect x="55" y="0" width="55" height="14" fill="#4d8f8b"/>
      <rect x="110" y="0" width="55" height="14" fill="#9fd2cd"/>
      <rect x="165" y="0" width="55" height="14" fill="#3f7f7c"/>
      <rect x="220" y="0" width="55" height="14" fill="#7a8a8f"/>
      <rect x="275" y="0" width="55" height="14" fill="#4fa39e"/>
    </g>
    <polygon points="0,400 330,345 330,470 0,752" fill="var(--teal-light)"/>
    <polygon points="0,400 330,372 330,395 210,465 0,465" fill="var(--teal-deep)"/>
    <polygon points="210,465 330,395 330,540" fill="var(--teal-dark)"/>
    <polygon points="0,700 0,752 60,752" fill="var(--teal-pale)"/>
    <g class="colour-strip">
      <rect x="0" y="752" width="110" height="28" fill="var(--teal-light)"/>
      <rect x="110" y="752" width="110" height="28" fill="var(--teal-mid)"/>
      <rect x="220" y="752" width="110" height="28" fill="var(--slate)"/>
    </g>
  </svg>

  <div class="services">
    <article class="service">
      <h2 class="service__title">Parenting</h2>
      <p class="service__text">Parenthood is an amazing journey, but for lots of people it raises all sorts of issues from fear of birth, breastfeeding difficulties and settling problems, to toddler discipline and food fussiness all the way through to getting help for your depressed or anxious adolescent. Our Parenting Psychologists can help you be the best parent you can be which will in turn lead to happier families, homes, children and parents.</p>
    </article>
    <article class="service">
      <h2 class="service__title">Chronic illness/pain</h2>
      <p class="service__text">Diabetes, heart disease, arthritis, asthma, migraines, dizziness, chronic fatigue syndrome, infertility, and PCOS are just some of the conditions that can be managed with psychological interventions. Everything we do is about helping you to manage your condition and get back to focusing on what you really want your life to be about.</p>
    </article>
    <article class="service">
      <h2 class="service__title">Eating</h2>
      <p class="service__text">Whether you suffer from anorexia, bulimia or binge eating, our strategies help you develop a healthy relationship with food and your body. The practical tips and strategies that we can provide are very useful for people undergoing lapband surgery or liposuction.</p>
    </article>
  </div>

  <p class="contact contact--web back-web">
    <svg width="12" height="12" viewBox="0 0 12 12"><circle cx="6" cy="6" r="5.3" fill="#fff"/><path d="M1 6h10M6 1c-2 2.5-2 7.5 0 10M6 1c2 2.5 2 7.5 0 10" stroke="var(--teal-deep)" stroke-width=".8" fill="none"/></svg>
    wellgrovemindclinic.com.au
  </p>
  <p class="contact back-address">
    <svg width="9" height="12" viewBox="0 0 9 12"><path d="M4.5 11.5C1.5 7.5.8 6 .8 4.3a3.7 3.7 0 017.4 0c0 1.7-.7 3.2-3.7 7.2z" fill="#fff"/><circle cx="4.5" cy="4.3" r="1.3" fill="var(--teal-light)"/></svg>
    <span>Suite 2/1187 Ferntree Rd,<br>Ashbury Vale 3142</span>
  </p>
  <p class="contact contact--phone back-phone">
    <svg width="8" height="13" viewBox="0 0 8 13"><path d="M6 1.5c-3 1-4 6 0 10" stroke="#fff" stroke-width="2" fill="none" stroke-linecap="round"/></svg>
    9362 5184
  </p>

  <div class="brand brand--large" style="left:140px;top:655px"><span class="brand__dot"></span><span>Wellgrove<br>Mind<br>Clinic</span></div>
</section>

</body>
</html>
```